Conservative, Modern and Sharp Builder Business card

Hi there,
We would like to update our existing business card.
I have attached photos of existing business card, logo and van sign.

I would like the business card to also list what we do :
Renovation • New Build • Alteration
Extension • Bathroom • Maintenance.(Seperated by dots)

Contact number : 021 0483 0752
(With that exact spacing)

Ideally when people looking from about 2-3 metres, they know that it is a builder’s business card

Open to suggestions on fonts, layout, style of business card

PLEASE ONLY SUBMIT YOUR BEST OR MAX 3 DESIGNS FOR EACH DESIGNER

Thanks

Industry/Entity Type

Construction. Renovation

Contact Information for Business Card

Details should be the same as the existing card. And addition of what we do.

Requirements
Should not have
• The new business card must not have the same layout as our existing one. Thanks

```html
<!DOCTYPE html>
<html lang="en">
<head>
<meta charset="UTF-8">
<title>KeelBuild Business Card</title>
<link rel="stylesheet" href="https://fonts.googleapis.com/css2?family=Poppins:wght@700&family=Inter:wght@400;600&display=swap">
<style>
  :root {
    --canvas: #e9e7e4;
    --ink: #111111;
    --card-dark: #161616;
    --card-light: #fafafa;
    --ghost-dark: #232323;
    --ghost-light: #efefef;
    --muted: #3a3a3a;
    --rule: #9a9a9a;
  }
  * { box-sizing: border-box; margin: 0; padding: 0; }
  html, body { width: 1200px; height: 900px; overflow: hidden; }
  body {
    background: var(--canvas);
    font-family: "Inter", Arial, sans-serif;
    position: relative;
  }
  .card {
    position: absolute;
    left: 250px;
    width: 700px;
    height: 400px;
    border-radius: 0 48px 0 48px;
    overflow: hidden;
    box-shadow: 0 10px 30px rgba(0,0,0,0.18);
  }
  .card-front { top: 40px; background: var(--card-dark); color: #fff; }
  .card-back { top: 460px; background: var(--card-light); color: var(--ink); }

  .ghost-square {
    position: absolute;
    top: 24px;
    right: 60px;
    width: 220px;
    height: 170px;
  }
  .card-front .ghost-square { width: 280px; height: 230px; }
  .card-front .ghost-square { background: var(--ghost-dark); }
  .card-back .ghost-square { background: var(--ghost-light); }

  .brand {
    position: absolute;
    left: 56px;
    bottom: 46px;
    display: flex;
    flex-direction: column;
    align-items: flex-start;
    gap: 14px;
  }
  .brand-square {
    width: 30px;
    height: 30px;
    background: currentColor;
  }
  .brand-name {
    font-family: "Poppins", Arial, sans-serif;
    font-weight: 700;
    font-size: 68px;
    line-height: 1;
    letter-spacing: -0.5px;
  }
  .card-back .brand { left: 56px; bottom: 40px; gap: 12px; }
  .card-back .brand-name { font-size: 52px; }

  .person {
    position: absolute;
    left: 56px;
    top: 44px;
  }
  .person-name {
    font-weight: 600;
    font-size: 18px;
    letter-spacing: 0.5px;
    text-transform: uppercase;
  }
  .person-role {
    margin-top: 6px;
    font-size: 16px;
    color: var(--muted);
  }
  .services {
    position: absolute;
    left: 56px;
    top: 112px;
    font-size: 13px;
    line-height: 1.6;
    color: var(--muted);
    letter-spacing: 0.2px;
  }

  .divider {
    position: absolute;
    left: 420px;
    top: 212px;
    width: 1px;
    height: 148px;
    background: var(--rule);
  }
  .contact-list {
    position: absolute;
    left: 440px;
    top: 210px;
    list-style: none;
    display: flex;
    flex-direction: column;
    gap: 9px;
    font-size: 17px;
  }
  .contact-list li { display: flex; align-items: center; gap: 8px; white-space: nowrap; }
  .contact-list .phone { font-weight: 600; font-size: 21px; }
  .contact-icon { width: 16px; height: 16px; flex: none; }
</style>
</head>
<body>
  <section class="card card-front">
    <div class="ghost-square"></div>
    <div class="brand">
      <span class="brand-square"></span>
      <span class="brand-name">KeelBuild</span>
    </div>
  </section>

  <section class="card card-back">
    <div class="ghost-square"></div>
    <div class="person">
      <p class="person-name">Marin Tolvey</p>
      <p class="person-role">Residential Builder</p>
    </div>
    <p class="services">Renovation • New Build • Alteration<br>Extension • Bathroom • Maintenance</p>
    <div class="brand">
      <span class="brand-square"></span>
      <span class="brand-name">KeelBuild</span>
    </div>
    <div class="divider"></div>
    <ul class="contact-list">
      <li class="phone">
        <svg class="contact-icon" viewBox="0 0 16 16"><path d="M4 1l2.5 3.5-1.5 1.5c.8 2 2.6 3.8 4.6 4.6l1.5-1.5L14.6 11.5 13 14c-6 0-11-5-11-11z" fill="#111"/></svg>
        021 0483 0752
      </li>
      <li>
        <svg class="contact-icon" viewBox="0 0 16 16"><rect x="1" y="3.5" width="14" height="10" rx="1" fill="#111"/><path d="M1.5 4l6.5 5 6.5-5" stroke="#fff" stroke-width="1.3" fill="none"/></svg>
        KeelBuild@outlook.com
      </li>
      <li>
        <svg class="contact-icon" viewBox="0 0 16 16"><circle cx="8" cy="8" r="6.3" stroke="#111" stroke-width="1.4" fill="none"/><ellipse cx="8" cy="8" rx="2.6" ry="6.3" stroke="#111" stroke-width="1.2" fill="none"/><path d="M1.8 8h12.4" stroke="#111" stroke-width="1.2"/></svg>
        www.KeelBuild.nz
      </li>
      <li>
        <svg class="contact-icon" viewBox="0 0 16 16"><circle cx="8" cy="8" r="6.3" stroke="#111" stroke-width="1.4" fill="none"/></svg>
        KeelBuild.nz
      </li>
    </ul>
  </section>
</body>
</html>
```